halbrook paving works

Needs to have phone number 0418352790 and email carlwhitby@mailnest.com.au.
ABN 27813046652
name carl whitby

For all your concreting solutions
Excavation
Exposed & colour concrete
House & shed slabs
Driveways
Landing & steps

Contact Information for Business Card

ph 0418352790
email carlwhitby@mailnest.com.au.
ABN 27813046652
name carl whitby

```html
<!DOCTYPE html>
<html lang="en">
<head>
<meta charset="utf-8">
<title>Halbrook Paving Works – Business Card</title>
<link href="https://fonts.googleapis.com/css2?family=Montserrat:wght@400;500;600;700&display=swap" rel="stylesheet">
<style>
:root{
  --bg:#262627;
  --slate:#5b5b5d;
  --slate-dark:#4e4e50;
  --orange:#f26a21;
  --white:#ffffff;
  --ink:#4a4a4c;
}
*{margin:0;padding:0;box-sizing:border-box}
html,body{width:1200px;height:903px;overflow:hidden;background:var(--bg);font-family:"Montserrat",sans-serif}
.stage{position:relative;width:1200px;height:903px}
.card{position:absolute;width:520px;height:300px;border-radius:18px;overflow:hidden}

/* back */
.card-back{left:80px;top:110px;background:var(--slate)}
.card-back .brand{position:absolute;left:40px;top:112px;display:flex;align-items:center;gap:10px;width:170px}
.brand-square{width:16px;height:16px;background:var(--orange);flex:none}
.card-back .brand-name{color:var(--white);font-weight:700;font-size:15px;line-height:1.25;text-transform:uppercase;letter-spacing:.5px}
.divider{position:absolute;left:228px;top:70px;width:1.5px;height:160px;background:#c9c9c9}
.services{position:absolute;left:252px;top:72px;color:var(--white)}
.services h2{font-size:15px;font-weight:700;text-transform:uppercase;letter-spacing:.6px;margin-bottom:8px}
.services ul{list-style:none}
.services li{font-size:13.5px;font-weight:500;text-transform:uppercase;letter-spacing:.6px;line-height:24px;display:flex;align-items:center;gap:10px}
.services li::before{content:"";width:8px;height:8px;background:var(--orange);flex:none}

/* front */
.card-front{left:600px;top:480px;background:var(--white)}
.front-band{position:absolute;inset:0}
.front-brand{position:absolute;left:36px;top:74px;display:flex;align-items:center;gap:10px}
.front-brand .brand-name{color:var(--orange);font-weight:700;font-size:20px;text-transform:uppercase;letter-spacing:.6px}
.contact{position:absolute;left:36px;top:168px;color:var(--white)}
.person-name{color:var(--orange);font-size:19px;font-weight:700;text-transform:uppercase;letter-spacing:.8px}
.person-role{font-size:13px;font-weight:500;margin-bottom:8px}
.abn{font-size:13px;font-weight:500;margin-bottom:6px}
.abn b{font-weight:700}
.line{display:flex;align-items:center;gap:8px;font-size:13px;font-weight:500;line-height:20px}
.line svg{width:13px;height:13px;flex:none}
.edge-tab{position:absolute;left:0;top:196px;width:8px;height:36px;background:var(--orange);border-radius:0 6px 6px 0}
</style>
</head>
<body>
<main class="stage">
  <section class="card card-back" aria-label="Business card back">
    <div class="brand"><span class="brand-square"></span><span class="brand-name">Halbrook Paving Works</span></div>
    <div class="divider"></div>
    <div class="services">
      <h2>For all your concreting solutions</h2>
      <ul>
        <li>Excavation</li>
        <li>Exposed &amp; colour concrete</li>
        <li>House &amp; shed slabs</li>
        <li>Driveways</li>
        <li>Landing &amp; steps</li>
      </ul>
    </div>
  </section>

  <section class="card card-front" aria-label="Business card front">
    <svg class="front-band" viewBox="0 0 520 300" preserveAspectRatio="none" aria-hidden="true">
      <polygon points="0,160 300,160 340,110 520,110 520,300 0,300" fill="var(--slate)"/>
      <polygon points="400,0 520,0 520,110 470,110" fill="var(--orange)"/>
    </svg>
    <div class="front-brand"><span class="brand-square"></span><span class="brand-name">Halbrook Paving Works</span></div>
    <div class="edge-tab"></div>
    <div class="contact">
      <div class="person-name">Carl Whitby</div>
      <div class="person-role">Managing Director</div>
      <div class="abn"><b>ABN</b> 27813046652</div>
      <div class="line">
        <svg viewBox="0 0 24 24"><path fill="var(--orange)" d="M6.6 10.8a15 15 0 0 0 6.6 6.6l2.2-2.2a1 1 0 0 1 1-.25 11.4 11.4 0 0 0 3.6.57 1 1 0 0 1 1 1V20a1 1 0 0 1-1 1A17 17 0 0 1 3 4a1 1 0 0 1 1-1h3.5a1 1 0 0 1 1 1c0 1.25.2 2.45.57 3.57a1 1 0 0 1-.25 1z"/></svg>
        0418 352 790
      </div>
      <div class="line">
        <svg viewBox="0 0 24 24"><rect x="2" y="5" width="20" height="14" fill="var(--orange)"/><path d="M2 5l10 8 10-8" stroke="var(--slate)" stroke-width="2" fill="none"/></svg>
        carlwhitby@mailnest.com.au
      </div>
    </div>
  </section>
</main>
</body>
</html>
```